Golf Lesson Flyer Looking to attract Golfers with Emotion

I need an easy to read flyer that draws attention to golfers and convinces them to take golf lessons. I’m looking to attract golfers by appealing to their emotional sides of how much they love the game or how bad they currently play. I’m open for anything. I just want that to be easily seen on the flyer. The pricing isn’t as important to be seen.I included different styles of logos that could be used but don't have to be. The only one that has to be used is the Cedar Hollow Logo because that's where the lessons are given. The pricing is included in the pdf.

Target Market(s)

Golfers in Salt Lake City, Utah

Font styles to use
Sans Serif
Decorative

Colors
ec1f27
ffffff

Requirements
Must have
• Project must have "Cedar Hollow Teaching Academy" on the top of the list and use the Cedar Hollow logo. I would the hook of emotion easy to read. I don't care if the prices are the thing highlighted on the flyer. I want to catch peoples attention.
Nice to have
• I included my logo in several different styles. You can choose whichever one fits your design. Red, black, and white would be the preferable colors.
Should not have
• I don't want the focus to be on the prices.

```html
<!DOCTYPE html>
<html lang="en">
<head>
<meta charset="utf-8">
<title>Cedar Hollow Teaching Academy – Golf Lessons Flyer</title>
<link rel="stylesheet" href="https://fonts.googleapis.com/css2?family=Russo+One&family=Open+Sans:wght@400;600;700;800&display=swap">
<style>
  :root {
    --red: #ec1f27;
    --black: #111111;
    --white: #ffffff;
    --stage: #8fa8ae;
    --green: #2e7d32;
    --photo-dark: #3a3a3a;
    --photo-light: #d6d6d6;
  }
  * { box-sizing: border-box; margin: 0; padding: 0; }
  html, body { width: 1200px; height: 1000px; overflow: hidden; }
  body { background: var(--stage); font-family: "Open Sans", Arial, sans-serif; color: var(--black); }

  .flyer {
    position: absolute; left: 265px; top: 66px; width: 670px; height: 868px;
    background: var(--white); overflow: hidden;
  }
  .abs { position: absolute; }

  .venue { left: 0; width: 100%; top: 18px; text-align: center; }
  .venue-mark { display: inline-block; width: 12px; height: 12px; border-radius: 50%; background: var(--green); margin-bottom: 4px; }
  .venue-name { display: block; font-weight: 800; font-size: 11px; letter-spacing: 0.5px; color: var(--green); }
  .venue-tag { display: block; font-size: 5px; color: var(--green); letter-spacing: 0.5px; }

  .academy {
    left: 148px; top: 68px; width: 374px; height: 30px;
    border: 2px solid var(--black); text-align: center; white-space: nowrap;
    font-family: "Russo One", Arial, sans-serif; font-size: 16.5px; line-height: 26px; letter-spacing: 0.2px;
  }
  .coach {
    left: 0; width: 100%; top: 108px; text-align: center; white-space: nowrap;
    font-family: "Russo One", Arial, sans-serif; font-weight: 400; font-size: 34px; line-height: 44px; letter-spacing: 0.5px;
  }
  .awards { left: 0; top: 160px; width: 670px; height: 68px; }

  .hook {
    left: 0; top: 244px; width: 670px; height: 152px; background: var(--red);
    display: flex; align-items: center; justify-content: center; text-align: center;
    font-family: "Open Sans", Arial, sans-serif; font-weight: 800; color: var(--white);
    font-size: 27px; line-height: 36px; text-shadow: 3px 3px 0 var(--black); white-space: nowrap;
  }

  .lower { left: 0; top: 396px; width: 670px; height: 472px; }

  .includes {
    left: 43px; top: 404px; width: 586px; height: 29px;
    border-top: 2px solid var(--black); border-bottom: 2px solid var(--black);
    text-align: center; font-weight: 700; font-size: 16px; line-height: 25px; letter-spacing: 0.3px; white-space: nowrap;
  }

  .rates { left: 43px; top: 462px; width: 428px; }
  .rate-heads { display: grid; grid-template-columns: repeat(4, 1fr); font-weight: 700; font-size: 10px; text-align: center; height: 18px; }
  .tier-bar { color: var(--white); font-weight: 700; font-size: 12px; text-align: center; height: 19px; line-height: 19px; }
  .tier-bar.pro { background: var(--red); }
  .tier-bar.apprentice { background: var(--black); margin-top: 2px; }
  .rate-row { display: grid; grid-template-columns: repeat(4, 1fr); gap: 4px; }
  .rate-cell {
    background: var(--white); border: 2px solid var(--black); border-top: 0;
    display: flex; flex-direction: column; justify-content: center; align-items: center;
    font-size: 10.5px; line-height: 12.5px; text-align: center; padding: 3px 4px;
  }
  .rate-row.pro .rate-cell { height: 70px; border-left: 3px solid var(--red); border-right: 3px solid var(--red); }
  .rate-row.pro .rate-cell:first-child { border-left: 2px solid var(--black); }
  .rate-row.apprentice .rate-cell { height: 76px; }
  .rate-row.apprentice .rate-cell:last-child { clip-path: polygon(0 0,100% 0,100% 85%,92% 100%,0 100%); }
  .rate-cell hr { width: 80%; border: 0; border-top: 1px solid var(--black); margin: 3px 0; }

  .extras { left: 43px; top: 674px; font-weight: 800; font-size: 10px; line-height: 17px; }

  .schedule {
    left: 23px; top: 810px; color: var(--white); font-weight: 700; text-align: center;
    font-size: 14px; line-height: 20px; letter-spacing: 0.5px;
  }
  .schedule span { display: block; font-size: 19px; letter-spacing: 2px; }
  .contact-divider { left: 137px; top: 804px; width: 1px; height: 52px; background: var(--white); }
  .contacts { left: 145px; top: 802px; color: var(--white); font-size: 11px; line-height: 19.5px; }
  .contacts li { list-style: none; display: flex; align-items: center; gap: 6px; }
  .contacts li:first-child { font-size: 13px; }
  .contacts svg { width: 11px; height: 11px; fill: var(--white); }
</style>
</head>
<body>
<main class="flyer">
  <div class="abs venue">
    <span class="venue-mark"></span>
    <span class="venue-name">CEDAR HOLLOW</span>
    <span class="venue-tag">PUBLIC GOLF COURSE</span>
  </div>

  <div class="abs academy">CEDAR HOLLOW TEACHING ACADEMY</div>
  <h1 class="abs coach">DANE MERCER, TGP</h1>

  <svg class="abs awards" viewBox="0 0 670 68" aria-label="Award badges">
    <rect x="178" y="4" width="94" height="60" rx="6" fill="#e6e6e6"/>
    <circle cx="333" cy="34" r="10" fill="var(--black)"/>
    <rect x="394" y="4" width="94" height="60" rx="6" fill="#e6e6e6"/>
  </svg>

  <div class="abs hook">
    <p>FRUSTRATED YOU DON'T KNOW HOW TO<br>ACHIEVE YOUR GOALS?<br>GET A BLUEPRINT THAT SHOWS YOU HOW</p>
  </div>

  <svg class="abs lower" viewBox="0 0 670 472">
    <defs>
      <linearGradient id="fog" x1="0" y1="0" x2="0" y2="1">
        <stop offset="0" stop-color="#ffffff"/>
        <stop offset="0.55" stop-color="#ededed"/>
        <stop offset="1" stop-color="#c9c9c9"/>
      </linearGradient>
      <linearGradient id="photo" x1="0" y1="0" x2="0" y2="1">
        <stop offset="0" stop-color="var(--photo-light)"/>
        <stop offset="0.6" stop-color="#9a9a9a"/>
        <stop offset="1" stop-color="var(--photo-dark)"/>
      </linearGradient>
    </defs>
    <rect width="670" height="472" fill="url(#fog)"/>
    <polygon points="670,4 670,472 385,472" fill="url(#photo)" role="img" aria-label="Black and white photo of a golfer in red shorts finishing his swing on a course"/>
    <polygon points="0,346 427,404 385,472 0,472" fill="var(--black)"/>
  </svg>

  <div class="abs includes">LESSONS INCLUDE A VIDEO SUMMARY AND A SWINGLAB REPORT</div>

  <section class="abs rates">
    <div class="rate-heads"><span>ADULT RATES</span><span>ADULT PACKAGES</span><span>JUNIOR RATES</span><span>12 &amp; UNDER</span></div>
    <div class="tier-bar pro">DANE</div>
    <div class="rate-row pro">
      <div class="rate-cell">3 HOUR (HALF DAY) $300<hr>50 MIN $120<hr>30 MIN $60</div>
      <div class="rate-cell">5 x 50 MIN<br>$500 ($100 EACH)</div>
      <div class="rate-cell">45 MIN $70<hr>5 x 45 MIN<br>$300 ($60 EACH)</div>
      <div class="rate-cell">30 MIN $50</div>
    </div>
    <div class="tier-bar apprentice">APPRENTICE</div>
    <div class="rate-row apprentice">
      <div class="rate-cell">50 MIN $60<hr>30 MIN $30</div>
      <div class="rate-cell">3 x 50 MIN $165<br>($55 EACH)<hr>5 x 50 MIN $250<br>($50 EACH)</div>
      <div class="rate-cell">45 MIN $30<hr>5 x 45 MIN<br>$150 ($30 EACH)</div>
      <div class="rate-cell">30 MIN $20</div>
    </div>
  </section>

  <p class="abs extras">SWINGLAB USAGE WITH NO INSTRUCTION: $80<br>ONLINE LESSONS: $40</p>

  <p class="abs schedule">TO SCHEDULE<span>LESSONS</span></p>
  <div class="abs contact-divider"></div>
  <ul class="abs contacts">
    <li><svg viewBox="0 0 24 24"><path d="M6.6 10.8a15 15 0 0 0 6.6 6.6l2.2-2.2c.3-.3.7-.4 1-.2 1.1.4 2.3.6 3.6.6.6 0 1 .4 1 1V20c0 .6-.4 1-1 1A17 17 0 0 1 3 4c0-.6.4-1 1-1h3.5c.6 0 1 .4 1 1 0 1.3.2 2.5.6 3.6.1.3 0 .7-.2 1z"/></svg>435-555-0174</li>
    <li><svg viewBox="0 0 24 24"><path d="M2 5h20v14H2zm2 2v.5l8 5 8-5V7z"/></svg>DANEMERCERGOLF@EXAMPLE.COM</li>
    <li><svg viewBox="0 0 24 24"><path d="M12 2a10 10 0 1 0 0 20 10 10 0 0 0 0-20zm1 2.1c1.3.9 2.3 3 2.6 5.9H13zm-2 0V10H8.4c.3-2.9 1.3-5 2.6-5.9zM4.1 10a8 8 0 0 1 4.3-5.4A12 12 0 0 0 6.4 10zm0 4h2.3a12 12 0 0 0 2 5.4A8 8 0 0 1 4.1 14zm4.3 0H11v5.9c-1.3-.9-2.3-3-2.6-5.9zM13 14h2.6c-.3 2.9-1.3 5-2.6 5.9zm2.6 5.4a12 12 0 0 0 2-5.4h2.3a8 8 0 0 1-4.3 5.4zM17.6 10a12 12 0 0 0-2-5.4 8 8 0 0 1 4.3 5.4z"/></svg>WWW.DANEMERCERGOLF.COM</li>
  </ul>
</main>
</body>
</html>
```